Flooring & Interior Design showroom

Just bought this business- Maple Terrace Flooring & Interiors. Love our logo (we are on Maple Terrace )and colors
Forest green, gold and black
Love that the back lists everything we do. We no longer have stonavelle but need to add in LVP/ SPC and need to take out tirelli shadehouse logo at the bottom and use the zumo logo instead (maybe? open to suggestions)

Not in love with our cards- I want a higher end look
I hate the gradient poop color we have now.
Would love if they were all black - maybe or ??
or had a foil or embossing?

```html
<!DOCTYPE html>
<html lang="en">
<head>
<meta charset="utf-8">
<title>Maple Terrace Flooring &amp; Interiors — Stationery</title>
<link href="https://fonts.googleapis.com/css2?family=Lato:wght@400;700&family=Pinyon+Script&display=swap" rel="stylesheet">
<style>
  :root{
    --backdrop:#e4e4e4;
    --paper:#f5f5f5;
    --forest:#1f5a36;
    --forest-dark:#173f27;
    --forest-light:#3a7a4c;
    --gold:#c9a13b;
    --card-black:#2b2a2a;
    --ink:#1f1f1f;
    --muted:#6b6b6b;
    --window:#cfcfcf;
  }
  *{box-sizing:border-box;margin:0;padding:0}
  html,body{width:1200px;height:942px;overflow:hidden}
  body{background:var(--backdrop);font-family:"Lato",sans-serif;color:var(--ink);position:relative;-webkit-font-smoothing:antialiased;-moz-osx-font-smoothing:grayscale;text-rendering:geometricPrecision}

  .brand{display:flex;align-items:center;gap:6px;font-family:"Lato",sans-serif;font-weight:700;color:var(--forest);white-space:nowrap}
  .brand-mark{display:block;background:currentColor}

  /* Letterhead */
  .letterhead{position:absolute;left:157px;top:150px;width:436px;height:617px;background:var(--paper);box-shadow:0 1px 4px rgba(0,0,0,.12)}
  .letterhead .brand{position:absolute;left:32px;top:38px;font-size:15px}
  .letterhead .brand-mark{width:10px;height:10px}
  .lh-contact{position:absolute;top:36px;right:20px;display:flex;gap:6px;font-size:6.6px;line-height:8.8px;color:var(--muted);white-space:nowrap}
  .lh-address{text-align:right;padding-right:6px;border-right:1px solid #bbb}
  .lh-lines{list-style:none}
  .lh-lines li{display:flex;align-items:center;gap:4px}
  .ico{width:6px;height:6px;fill:var(--forest);flex:none}
  .letter{position:absolute;left:46px;top:205px;width:343px;font-size:7.2px;line-height:8.8px;text-align:justify;color:var(--ink)}
  .letter .salutation{font-weight:700;margin-bottom:9px}
  .letter p{margin-bottom:8.8px;color:var(--ink)}
  .closing{position:absolute;left:46px;top:416px;font-size:7.2px;color:var(--ink)}
  .signature{font-family:"Pinyon Script",cursive;font-size:15px;margin-top:10px;line-height:16px}
  .role{line-height:8px}

  /* Business cards */
  .card{position:absolute;top:139px;width:227px;height:130px;background:var(--card-black);color:var(--gold);box-shadow:0 1px 4px rgba(0,0,0,.18);overflow:hidden}
  .card-front{left:625px}
  .card-back{left:897px}
  .card-front .brand{position:absolute;left:24px;top:58px;font-size:10.5px;color:var(--forest-light)}
  .card-front .brand-mark{width:7px;height:7px}
  .card-divider{position:absolute;left:113px;top:32px;width:1px;height:72px;background:#4a4a4a}
  .card-divider::before{content:"";position:absolute;top:0;left:-.5px;width:2px;height:10px;background:var(--gold)}
  .card-person{position:absolute;left:124px;top:31px;font-size:4.6px;line-height:6.4px;white-space:nowrap}
  .card-person .name{font-size:6.4px;font-weight:700;letter-spacing:.2px;line-height:7px}
  .card-person .title{margin-bottom:5px}
  .card-person .addr{margin-bottom:3px}
  .card-person ul{list-style:none}
  .card-person li{display:flex;align-items:center;gap:3px}
  .card-person .ico{width:4px;height:4px;fill:var(--gold)}

  .card-back .brand{position:absolute;left:22px;top:22px;font-size:9px;color:var(--forest-light)}
  .card-back .brand-mark{width:6px;height:6px}
  .partner{position:absolute;right:12px;top:15px;display:flex;flex-direction:column;align-items:center;gap:2px;font-size:3.8px;font-weight:700;color:#eee;white-space:nowrap}
  .partner-mark{width:15px;height:15px;border-radius:50%;background:#e07a22}
  .services-head{position:absolute;left:46px;top:52px;right:26px;display:flex;align-items:center;gap:4px;font-size:4.4px;font-weight:700}
  .services-head::after{content:"";flex:1;height:.6px;background:#6a6a6a}
  .services{position:absolute;left:46px;top:62px;display:flex;gap:22px;font-size:4.4px;line-height:6px}
  .services ul{list-style:none;white-space:nowrap;min-width:28px}
  .services li::before{content:"";display:inline-block;width:2px;height:2px;border-radius:50%;background:var(--gold);margin-right:3px;vertical-align:middle}
  .licence-bar{position:absolute;left:0;right:0;bottom:8px;height:12px;background:linear-gradient(90deg,#a8842a,var(--gold) 50%,#a8842a);color:var(--card-black);font-size:4.4px;font-weight:700;text-align:center;line-height:12px;white-space:nowrap}

  /* Envelopes */
  .envelope{position:absolute;left:624px;width:500px;height:217px;background:var(--paper);box-shadow:0 1px 4px rgba(0,0,0,.12);overflow:hidden}
  .envelope-front{top:298px}
  .envelope-front .brand{position:absolute;left:30px;top:40px;font-size:14px}
  .envelope-front .brand-mark{width:9px;height:9px}
  .env-address{position:absolute;left:49px;top:89px;font-size:6.8px;line-height:8.8px;color:var(--muted)}
  .env-window{position:absolute;left:315px;top:127px;width:158px;height:64px;border-radius:5px;border:1px solid #bdbdbd;background:linear-gradient(110deg,#c9c9c9,#e4e4e4 55%,#c6c6c6)}
  .envelope-back{top:550px}
  .env-flap{position:absolute;left:0;top:0;width:500px;height:75px}
  .envelope-back .brand{position:absolute;left:0;right:0;top:32px;justify-content:center;font-size:10.5px;color:#f2f2f2}
  .envelope-back .brand-mark{width:7px;height:7px}
</style>
</head>
<body>

<svg width="0" height="0" style="position:absolute" aria-hidden="true">
  <symbol id="i-phone" viewBox="0 0 10 10"><path d="M2 1l2 2-1 1.2c.6 1.2 1.6 2.2 2.8 2.8L7 6l2 2-1.3 1.3C4.5 9 1 5.5.7 2.3z"/></symbol>
  <symbol id="i-mobile" viewBox="0 0 10 10"><path d="M3 0h4a1 1 0 0 1 1 1v8a1 1 0 0 1-1 1H3a1 1 0 0 1-1-1V1a1 1 0 0 1 1-1zm0 1.5v6h4v-6z"/></symbol>
  <symbol id="i-fax" viewBox="0 0 10 10"><path d="M2.5 0h5v3h-5zM0 3.5h10v4H8V10H2V7.5H0zm3 3v2.5h4V6.5z"/></symbol>
  <symbol id="i-mail" viewBox="0 0 10 10"><path d="M0 2h10v6H0zm1 1 4 3 4-3z"/></symbol>
  <symbol id="i-web" viewBox="0 0 10 10"><path d="M5 0a5 5 0 1 0 0 10A5 5 0 0 0 5 0zm0 1c.7 0 1.4 1.5 1.5 3.5h-3C3.6 2.5 4.3 1 5 1zM3.5 5.5h3C6.4 7.5 5.7 9 5 9s-1.4-1.5-1.5-3.5z"/></symbol>
</svg>

<!-- Letterhead -->
<section class="letterhead">
  <div class="brand"><span class="brand-mark"></span>Maple Terrace</div>
  <div class="lh-contact">
    <div class="lh-address">
      Maple Terrace Flooring &amp; Interiors<br>
      314 Maple Terrace<br>
      Cedar Bluff CA 90001<br>
      www.mapleterraceflooring.com
    </div>
    <ul class="lh-lines">
      <li><svg class="ico"><use href="#i-phone"/></svg>555.201.0188</li>
      <li><svg class="ico"><use href="#i-mobile"/></svg>555.340.2277</li>
      <li><svg class="ico"><use href="#i-fax"/></svg>555.201.0199</li>
      <li><svg class="ico"><use href="#i-mail"/></svg>info@mapleterraceflooring.com</li>
    </ul>
  </div>
  <div class="letter">
    <div class="salutation">Dear Owen Redfield,</div>
    <p>Lorem ipsum dolor sit amet, consectetuer adipiscing elit, sed diam nonummy nibh euismod tincidunt ut laoreet dolore magna aliquam erat volutpat. Ut wisi enim ad minim veniam, quis nostrud exerci tation ullamcorper suscipit lobortis nisl ut aliquip ex ea commodo consequat. Duis dolore te feugait nulla facilisi. Nam liber tempor cum soluta nobis eleifend option congue nihil imperdiet doming id quod mazim placerat facer possim assum. Lorem ipsum dolor sit amet, consectetuer adipiscing elit, sed diam nonummy nibh euismod tincidunt ut laoreet dolore magna aliquam erat volutpat. Ut wisi enim ad minim veniam, quis nostrud exerci tation ullamcorper suscipit lobortis nisl ut aliquip ex ea commodo consequat.</p>
    <p>Consectetuer adipiscing elit, sed diam nonummy nibh euismod tincidunt ut laoreet dolore magna aliquam erat volutpat. Ut wisi enim ad minim veniam, quis nostrud exerci tation ullamcorper suscipit lobortis nisl ut aliquip ex ea commodo consequat. Consectetuer adipiscing elit, sed diam nonummy nibh euismod tincidunt ut laoreet dolore magna aliquam erat volutpat. Ut wisi enim ad minim veniam, quis nostrud exerci tation ullamcorper suscipit lobortis nisl ut aliquip ex ea commodo consequat.</p>
    <p>Consectetuer adipiscing elit, sed diam nonummy nibh euismod tincidunt ut laoreet dolore magna aliquam erat volutpat. Ut wisi enim ad minim veniam, quis nostrud exerci tation ullamcorper suscipit lobortis nisl ut aliquip ex ea commodo consequat. Consectetuer adipiscing elit, sed diam nonummy nibh euismod tincidunt ut laoreet dolore magna aliquam erat volutpat. Ut wisi enim ad minim veniam, quis nostrud exerci tation ullamcorper suscipit lobortis nisl ut aliquip ex ea commodo consequat.</p>
  </div>
  <div class="closing">
    Sincerely Yours
    <div class="signature">Calvin Hartwell</div>
    <div class="role">General Manager</div>
  </div>
</section>

<!-- Business card front -->
<section class="card card-front">
  <div class="brand"><span class="brand-mark"></span>Maple Terrace</div>
  <div class="card-divider"></div>
  <div class="card-person">
    <div class="name">LENA MARSH</div>
    <div class="title">Salesperson</div>
    <div class="addr">314 Maple Terrace<br>Cedar Bluff CA 90001</div>
    <ul>
      <li><svg class="ico"><use href="#i-phone"/></svg>555.201.0188</li>
      <li><svg class="ico"><use href="#i-mobile"/></svg>555.340.2277</li>
      <li><svg class="ico"><use href="#i-fax"/></svg>555.201.0199</li>
      <li><svg class="ico"><use href="#i-mail"/></svg>info@mapleterraceflooring.com</li>
      <li><svg class="ico"><use href="#i-web"/></svg>www.mapleterraceflooring.com</li>
    </ul>
  </div>
</section>

<!-- Business card back -->
<section class="card card-back">
  <div class="brand"><span class="brand-mark"></span>Maple Terrace</div>
  <div class="partner"><span class="partner-mark"></span>Larkwell Shades</div>
  <div class="services-head">OUR SERVICES</div>
  <div class="services">
    <ul><li>Area Rugs</li><li>Blinds</li><li>Carpet</li><li>Cork</li><li>Hardwood</li><li>Laminate</li><li>LVP / SPC</li></ul>
    <ul><li>Sheers</li><li>Valances</li><li>Vinyl</li><li>Bed Spreads</li><li>Draperies</li><li>Fabric</li></ul>
    <ul><li>Motorized Shades</li><li>Pillows</li><li>Shutters</li><li>Upholstery</li><li>Verticals</li></ul>
  </div>
  <div class="licence-bar">CA LIC #482913 | HOME TOWN SERVICE SINCE 1979</div>
</section>

<!-- Envelope front -->
<section class="envelope envelope-front">
  <div class="brand"><span class="brand-mark"></span>Maple Terrace</div>
  <div class="env-address">
    Maple Terrace Flooring &amp; Interiors<br>
    314 Maple Terrace<br>
    Cedar Bluff CA 90001
  </div>
  <div class="env-window"></div>
</section>

<!-- Envelope back -->
<section class="envelope envelope-back">
  <svg class="env-flap" viewBox="0 0 500 75" aria-hidden="true">
    <defs>
      <linearGradient id="flap" x1="0" x2="1">
        <stop offset="0" stop-color="#1c4d2e"/>
        <stop offset=".5" stop-color="#2f6a40"/>
        <stop offset="1" stop-color="#1c4d2e"/>
      </linearGradient>
    </defs>
    <path d="M0 0H500L488 58Q485 71 470 71H30Q15 71 12 58Z" fill="url(#flap)"/>
    <path d="M14 66Q8 72 8 85M486 66Q492 72 492 85" stroke="#d5d5d5" fill="none"/>
  </svg>
  <div class="brand"><span class="brand-mark"></span>Maple Terrace</div>
</section>

</body>
</html>
```